New Business Card Design Project

We are looking for a talented individual to create a truly awesome/unique business card design for us. We are looking for a someone to design something that will really stand out from the crowd - we don't mind what ideas you come up with (ie embossed/flat/matte/shine etc etc) just wow us with your creativity.
Updates

Target Market(s)

Video Games Industry Professionals (all levels of seniority from QA Testers through to CEOs)

Contact Information for Business Card

Company logo (see upload)
Company name: Northbay Play Careers Ltd
Employee Name: Darren Elsby
Job title: CEO
Website: www.nbpc2go.example
Office +44 1632 960418
Mobile: +44 7700 900276
Email: darren@nbpc2go.example

Colors

Designer to choose colors to be used in the design.

Requirements
Must have
• The business card design MUST contain all the information listed in the BUSINESS CARD DETAILS box.
• You will see the colours that are relevant to us (ie company logo) in the uploaded imagery - however you do not have to use all these colours when designing the business card itself
• MUST BE DOUBLE SIDED

```html
<!DOCTYPE html>
<html lang="en">
<head>
<meta charset="utf-8">
<title>Northbay Play Careers – Business Card</title>
<link href="https://fonts.googleapis.com/css2?family=Exo+2:wght@400;600&display=swap" rel="stylesheet">
<style>
  :root {
    --navy: #1d2d5c;
    --orange: #f47d22;
    --white: #ffffff;
    --paper: #ffffff;
  }
  * { box-sizing: border-box; margin: 0; padding: 0; }
  html, body { width: 1200px; height: 849px; overflow: hidden; background: var(--paper); }
  .sheet {
    position: relative; width: 1200px; height: 849px; overflow: hidden;
    font-family: "Exo 2", sans-serif; color: var(--white);
  }
  .label { position: absolute; color: var(--orange); font-size: 18px; line-height: 1; }
  .note { position: absolute; color: var(--orange); font-size: 15px; line-height: 22px; }

  .card {
    position: absolute; overflow: hidden; border-radius: 10px;
    background: var(--navy);
  }
  .card--front .band { position: absolute; left: 0; right: 0; bottom: 0; background: var(--orange); }
  .card--back .band { position: absolute; left: 0; right: 0; top: 0; background: var(--orange); }

  .mascot {
    position: absolute; border-radius: 40% 45% 40% 50%;
    background: linear-gradient(135deg, var(--orange) 0%, #f7f2ee 45%, #3a4a78 100%);
  }
  .wordmark { position: absolute; font-weight: 600; white-space: nowrap; }
  .lines { position: absolute; white-space: nowrap; }
  .lines .strong { font-weight: 600; }

  /* large front */
  .front-lg { left: 62px; top: 56px; width: 490px; height: 317px; }
  .front-lg .band { height: 107px; }
  .front-lg .mascot { left: 14px; top: 120px; width: 180px; height: 132px; }
  .front-lg .wordmark { left: 206px; top: 170px; font-size: 34px; line-height: 36px; }

  /* large back */
  .back-lg { left: 598px; top: 56px; width: 490px; height: 317px; }
  .back-lg .band { height: 108px; }
  .back-lg .mascot { left: 358px; top: 52px; width: 116px; height: 92px; }
  .back-lg .lines { left: 20px; font-size: 23px; line-height: 29px; }
  .back-lg .lines--company { top: 10px; }
  .back-lg .lines--person { top: 186px; }

  /* small front */
  .front-sm { left: 54px; top: 493px; width: 389px; height: 251px; }
  .front-sm .band { height: 85px; }
  .front-sm .mascot { left: 12px; top: 95px; width: 142px; height: 104px; }
  .front-sm .wordmark { left: 165px; top: 136px; font-size: 27px; line-height: 29px; }

  /* seam edge */
  .seam {
    position: absolute; left: 457px; top: 493px; width: 9px; height: 251px;
    background: linear-gradient(90deg, var(--navy) 0 33%, var(--orange) 33% 67%, var(--navy) 67%);
  }

  /* small back */
  .back-sm { left: 480px; top: 493px; width: 388px; height: 251px; }
  .back-sm .band { height: 85px; }
  .back-sm .mascot { left: 284px; top: 40px; width: 92px; height: 75px; }
  .back-sm .lines { left: 16px; font-size: 18px; line-height: 23px; }
  .back-sm .lines--company { top: 7px; }
  .back-sm .lines--person { top: 148px; }

  .leaders { position: absolute; left: 0; top: 0; }

  .side-band {
    position: absolute; left: 1148px; top: 0; width: 52px; height: 849px;
    background: linear-gradient(var(--orange) 0 253px, var(--navy) 253px);
  }
  .side-band__name {
    position: absolute; left: 1176px; top: 356px;
    transform-origin: 0 0; transform: rotate(90deg) translateY(-50%);
    font-size: 25px; white-space: nowrap; color: var(--white);
  }
</style>
</head>
<body>
<div class="sheet">
  <div class="label" style="left:68px; top:29px;">Front</div>
  <div class="label" style="left:601px; top:29px;">Back</div>

  <div class="card card--front front-lg">
    <div class="band"></div>
    <div class="mascot" role="img" aria-label="Company mascot illustration"></div>
    <div class="wordmark">Northbay Play<br>Careers</div>
  </div>

  <div class="card card--back back-lg">
    <div class="band"></div>
    <div class="lines lines--company">
      <div class="strong">Northbay Play Careers Ltd</div>
      <div>www.nbpc2go.example</div>
      <div>+44 1632 960418</div>
    </div>
    <div class="mascot" role="img" aria-label="Company mascot illustration"></div>
    <div class="lines lines--person">
      <div class="strong">Darren Elsby</div>
      <div>CEO</div>
      <div>Mobile: +44 7700 900276</div>
      <div>Email: darren@nbpc2go.example</div>
    </div>
  </div>

  <div class="card card--front front-sm">
    <div class="band"></div>
    <div class="mascot" role="img" aria-label="Company mascot illustration"></div>
    <div class="wordmark">Northbay Play<br>Careers</div>
  </div>

  <div class="seam"></div>

  <div class="card card--back back-sm">
    <div class="band"></div>
    <div class="lines lines--company">
      <div class="strong">Northbay Play Careers Ltd</div>
      <div>www.nbpc2go.example</div>
      <div>+44 1632 960418</div>
    </div>
    <div class="mascot" role="img" aria-label="Company mascot illustration"></div>
    <div class="lines lines--person">
      <div class="strong">Darren Elsby</div>
      <div>CEO</div>
      <div>Mobile: +44 7700 900276</div>
      <div>Email: darren@nbpc2go.example</div>
    </div>
  </div>

  <svg class="leaders" width="1200" height="849" viewBox="0 0 1200 849" fill="none" stroke="#1d2d5c" stroke-width="1.2">
    <path d="M456 452 C448 462 452 472 468 468 C486 464 492 475 492 498"/>
    <path d="M842 438 C900 470 880 520 836 540"/>
    <path d="M463 748 C470 766 490 766 512 762"/>
    <path d="M194 688 C250 720 275 760 240 775 C215 786 230 798 250 802"/>
  </svg>

  <div class="note" style="left:409px; top:424px;">3mm radius</div>
  <div class="note" style="left:652px; top:422px;">White part of logo with<br>an embossed finish</div>
  <div class="note" style="left:518px; top:751px;">Seamed card - with an<br>orange centre</div>
  <div class="note" style="left:264px; top:785px;">White text &amp; logo with<br>an embossed finish</div>

  <div class="side-band"></div>
  <div class="side-band__name">Northbay Play Careers Ltd</div>
</div>
</body>
</html>
```